Tasman Curdworks Guild needs new business cards

We need new business cards designed and produced. We are likely to need other design work done for ads, flyers etc in future.

We would like to start with an initial business card.

The Tasman Curdworks Guild (TCG) is a membership-based not-for-profit organisation that looks after the interests of Australia's small to medium artisan cheesemakers, many of whom are also small-scale farmers. The design should be simple, using our logo, but also communicate our artisan cheese and small dairy farm focus.

The first card to be designed and produced is for me, Miriam Tolhurst. My details are:

Miriam Tolhurst
Secretary
Tasman Curdworks Guild (TCG)
http://www.curdworksguild.example
T +61452837190
E miriam.miriamtolhurst@mailbox.example

I have attached the TCG logo in jpg form. I have a higher resolution version available if needed.

Thank you!

Miriam

Miriam Tolhurst
Tasman Curdworks Guild
miriam.miriamtolhurst@mailbox.example
+61452837190

Sans Serif

• Logo (see attached file)

```html
<!DOCTYPE html>
<html lang="en">
<head>
<meta charset="utf-8">
<title>Tasman Curdworks Guild — Business Card</title>
<link rel="stylesheet" href="https://fonts.googleapis.com/css2?family=Crimson+Text:wght@400;600&display=swap">
<style>
  :root {
    --bg: #2b2b2d;
    --paper: #ffffff;
    --brown: #5e3513;
    --brown-ink: #6b3d17;
    --cheese: #fbc55f;
    --cream: #f6e7c8;
    --white: #ffffff;
  }
  * { box-sizing: border-box; margin: 0; padding: 0; }
  html, body { width: 1200px; height: 886px; overflow: hidden; }
  body {
    background: var(--bg);
    font-family: "Crimson Text", Georgia, serif;
    display: flex;
    align-items: center;
    justify-content: center;
    gap: 60px;
  }
  .card { box-shadow: 0 14px 34px rgba(0,0,0,.45); flex: none; }

  /* Front */
  .card-front {
    width: 560px; height: 340px;
    background: var(--paper);
    display: flex; align-items: center; justify-content: center; gap: 22px;
  }
  .brand-dot {
    width: 66px; height: 66px; border-radius: 50%;
    background: var(--cheese);
    flex: none;
  }
  .brand-name {
    color: var(--brown-ink);
    font-size: 36px; line-height: 1.05; font-weight: 400;
    letter-spacing: .5px;
  }

  /* Back */
  .card-back {
    width: 340px; height: 560px;
    background: var(--cheese);
    padding: 18px;
  }
  .back-panel {
    width: 100%; height: 100%;
    background: var(--brown);
    border-radius: 26px;
    outline: 2px solid var(--cream);
    outline-offset: -7px;
    display: flex; flex-direction: column; align-items: center;
    padding: 76px 16px 44px;
    color: var(--white);
  }
  .icon-ring {
    width: 28px; height: 28px; border-radius: 50%;
    border: 1.5px solid var(--cheese);
    display: flex; align-items: center; justify-content: center;
    flex: none;
  }
  .icon-ring svg { width: 15px; height: 15px; fill: var(--cheese); }
  .person-name {
    margin-top: 14px;
    color: var(--cheese);
    font-size: 30px; font-weight: 600; letter-spacing: .5px;
    text-align: center;
  }
  .person-role { font-size: 19px; letter-spacing: .5px; margin-top: 2px; }
  .contact-list {
    list-style: none; margin-top: auto; width: 100%;
    display: flex; flex-direction: column; gap: 16px;
  }
  .contact-item {
    display: flex; align-items: center; gap: 8px;
    font-size: 12px; letter-spacing: 0;
    min-width: 0;
  }
  .contact-text { min-width: 0; overflow-wrap: anywhere; }
</style>
</head>
<body>
  <section class="card card-front" aria-label="Card front">
    <span class="brand-dot" aria-hidden="true"></span>
    <h1 class="brand-name">Tasman<br>Curdworks<br>Guild</h1>
  </section>

  <section class="card card-back" aria-label="Card back">
    <div class="back-panel">
      <span class="icon-ring" aria-hidden="true">
        <svg viewBox="0 0 16 16"><circle cx="8" cy="5" r="3"/><path d="M2 15c0-4 3-5.5 6-5.5s6 1.5 6 5.5z"/></svg>
      </span>
      <h2 class="person-name">Miriam Tolhurst</h2>
      <p class="person-role">Secretary</p>

      <ul class="contact-list">
        <li class="contact-item">
          <span class="icon-ring" aria-hidden="true">
            <svg viewBox="0 0 16 16"><path d="M4 1.5l2.2 3-1.3 1.6c.8 1.8 2.2 3.3 4 4.2l1.6-1.3 3 2.2-1.4 2.6C7 13.6 2.4 9 1.6 3z"/></svg>
          </span>
          <span class="contact-text">+61452837190</span>
        </li>
        <li class="contact-item">
          <span class="icon-ring" aria-hidden="true">
            <svg viewBox="0 0 16 16"><path d="M1.5 3.5h13v9h-13z M2.5 4.5l5.5 4.3 5.5-4.3" fill="none" stroke="#fbc55f" stroke-width="1.4"/></svg>
          </span>
          <span class="contact-text">miriam.miriamtolhurst@mailbox.example</span>
        </li>
        <li class="contact-item">
          <span class="icon-ring" aria-hidden="true">
            <svg viewBox="0 0 16 16"><g fill="none" stroke="#fbc55f" stroke-width="1.3"><circle cx="8" cy="8" r="6.2"/><ellipse cx="8" cy="8" rx="2.6" ry="6.2"/><path d="M1.8 8h12.4"/></g></svg>
          </span>
          <span class="contact-text">www.curdworksguild.example</span>
        </li>
      </ul>
    </div>
  </section>
</body>
</html>
```